New Website Design for Mesa Alta Coffee

Need a website design to be uploaded on Cartwell.com. Here are some of the sites I like:
https://grindlark.com
https://www.hollowmillcoffee.com
https://brevandcoffee.com

Coding

Coded - Design and coding required

Number of Pages Required

3 page

```html
<!DOCTYPE html>
<html lang="en">
<head>
<meta charset="utf-8">
<title>Mesa Alta Coffee</title>
<link rel="stylesheet" href="https://fonts.googleapis.com/css2?family=Playfair+Display:wght@700;800&family=Poppins:wght@300;400;500;600;700&display=swap">
<style>
:root{
  --orange:#d9622b;
  --amber:#f2a531;
  --brown:#4a2516;
  --brown-deep:#3a1c10;
  --rust:#a6431f;
  --ink:#2b1a12;
  --text:#555;
  --muted:#8a8a8a;
  --cream:#f6f1ea;
  --white:#fff;
  --line:#e6e0d8;
}
*{box-sizing:border-box;margin:0;padding:0}
html,body{width:1200px;height:5344px;overflow:hidden}
body{position:relative;background:var(--white);font-family:"Poppins",sans-serif;color:var(--text)}
.abs{position:absolute}
.photo{position:absolute}

/* top bar + nav */
.promo-bar{top:0;left:0;width:1200px;height:28px;background:var(--orange);color:#fff;font-size:11px;font-weight:600;letter-spacing:.5px;display:flex;align-items:center;justify-content:center}
.promo-bar u{margin-left:6px}
.site-nav{top:28px;left:0;width:1200px;height:92px;display:flex;align-items:center;padding:0 92px}
.brand{font-family:"Playfair Display",serif;font-weight:800;font-size:26px;color:var(--ink)}
.brand-light{color:#fff}
.menu{margin-left:auto;display:flex;gap:30px;font-size:13px;font-weight:600;color:var(--ink);letter-spacing:.3px;align-items:center}
.nav-icons{display:flex;gap:16px;margin-left:34px;align-items:center}
.cart-count{position:absolute;top:-6px;right:-7px;width:13px;height:13px;border-radius:50%;background:var(--orange);color:#fff;font-size:8px;display:flex;align-items:center;justify-content:center}

/* hero */
.hero{top:120px;left:0;width:1200px;height:700px;background:linear-gradient(100deg,#1c110c 0%,#3a241a 45%,#5a3a28 70%,#2a1a12 100%)}
.hero-title{top:330px;left:92px;color:#fff}
.hero-title h1{font-family:"Playfair Display",serif;font-size:72px;font-weight:800;line-height:1}
.hero-title h2{font-family:"Playfair Display",serif;font-size:44px;font-weight:700;line-height:1.2}
.hero-title p{font-size:15px;line-height:1.5;margin-top:18px;width:470px;color:#eee}
.btn{display:inline-block;background:var(--orange);color:#fff;font-size:12px;font-weight:600;letter-spacing:.6px;padding:12px 24px;border-radius:22px}
.hero .btn{margin-top:20px}

/* section heads */
.section-title{left:0;width:1200px;text-align:center;font-family:"Playfair Display",serif;font-weight:800;color:var(--ink);font-size:38px;line-height:1.2}

/* different */
.diff-band{top:1008px;left:90px;width:1020px;height:52px;background:var(--brown);border:3px solid var(--brown);outline:2px solid var(--brown);outline-offset:4px}
.feature{width:300px;display:flex;gap:16px;padding-bottom:20px;border-bottom:1px solid var(--line)}
.feature h4{font-size:15px;font-weight:600;color:var(--ink);margin-bottom:4px}
.feature p{font-size:12px;line-height:1.45;color:var(--muted)}
.ficon{flex:none;width:34px;height:34px}

/* eyebrow + copy */
.eyebrow{display:flex;align-items:center;gap:10px;font-size:11px;font-weight:600;letter-spacing:1px;color:var(--ink)}
.eyebrow::before{content:"";width:44px;height:2px;background:var(--ink)}
.copy h3{font-family:"Playfair Display",serif;font-weight:800;font-size:36px;line-height:1.15;color:var(--ink);margin:14px 0 16px}
.copy p{font-size:13px;line-height:1.7;color:var(--muted)}
.copy .btn{margin-top:24px}

/* cards */
.why{top:2080px;left:0;width:1200px;height:640px;background:var(--cream)}
.card{width:280px;background:#fff;box-shadow:0 6px 18px rgba(0,0,0,.06)}
.card .photo{position:relative;height:200px}
.card .body{padding:18px 20px 24px}
.card h4{font-size:15px;font-weight:600;color:var(--ink);line-height:1.35;margin-bottom:8px}
.card p{font-size:12px;line-height:1.5;color:var(--muted)}
.card .meta{font-size:10px;color:var(--muted);margin-bottom:6px}

/* band */
.band{top:3382px;left:90px;width:1020px;height:96px;background:var(--rust);display:flex;align-items:center;justify-content:space-between;padding:0 64px;color:#fff;font-family:"Playfair Display",serif;font-weight:700;font-size:32px;letter-spacing:.5px}

/* testimonial */
.quote{top:3720px;left:250px;width:700px;text-align:center;font-size:36px;font-weight:300;line-height:1.35;color:#444}
.quote-name{top:3880px;left:0;width:1200px;text-align:center;font-size:13px;font-weight:700;letter-spacing:1px;color:var(--ink)}
.dots{top:3720px;left:1178px;display:flex;flex-direction:column;gap:8px}
.dots i{width:9px;height:9px;border-radius:50%;background:#bbb;display:block}
.dots i:first-child{background:var(--ink)}

/* badges */
.badge{width:92px;height:92px;border-radius:50%;border:3px solid #999}

/* footer */
.foot-col h5{font-family:"Playfair Display",serif;font-weight:700;font-size:16px;color:var(--amber);letter-spacing:.8px;margin-bottom:16px}
.foot-col li{list-style:none;font-size:13px;color:#e8d9cf;line-height:1.9}
.contact-item{display:flex;gap:10px;margin-bottom:14px;font-size:12px;color:#e8d9cf;line-height:1.5}
.contact-item b{display:block;color:#fff;font-size:12px;letter-spacing:.5px}
.insta{display:grid;grid-template-columns:repeat(3,80px);gap:6px}
.insta div{height:80px}
.social{display:flex;gap:10px;margin-top:16px}
.social span{width:26px;height:26px;border-radius:50%;border:1px solid #e8d9cf}
.copyright{top:5282px;left:0;width:1200px;text-align:center;font-size:11px;color:#e8d9cf;letter-spacing:.5px}
</style>
</head>
<body>

<div class="abs promo-bar">FREE SHIPPING ON U.S. ORDERS OVER $50 <u>SHOP NOW</u></div>

<header class="abs site-nav">
  <div class="brand">Mesa Alta Coffee</div>
  <nav class="menu">
    <span>COFFEE SUBSCRIPTIONS</span><span>COFFEE GIFTS</span><span>COFFEE</span><span>COLD BREW</span><span>BLOG</span>
    <span class="nav-icons">
      <svg width="16" height="16" viewBox="0 0 16 16" fill="none" stroke="#2b1a12" stroke-width="1.6"><circle cx="8" cy="5" r="3"/><path d="M2 15c0-3.3 2.7-5 6-5s6 1.7 6 5"/></svg>
      <svg width="16" height="16" viewBox="0 0 16 16" fill="none" stroke="#2b1a12" stroke-width="1.6"><circle cx="7" cy="7" r="5"/><path d="M11 11l4 4"/></svg>
      <span style="position:relative"><svg width="18" height="16" viewBox="0 0 18 16" fill="none" stroke="#2b1a12" stroke-width="1.6"><path d="M1 1h3l2 10h9l2-7H5"/><circle cx="7" cy="14" r="1.2"/><circle cx="14" cy="14" r="1.2"/></svg><span class="cart-count">0</span></span>
    </span>
  </nav>
</header>

<section class="abs hero" role="img" aria-label="Hand pouring coffee from a copper pot in a dim cafe"></section>
<div class="abs hero-title">
  <h1>Mornings</h1>
  <h2>Never Tasted So Good.</h2>
  <p>Start your morning with the world's best coffees. Explore our coffee subscription options starting at $16.50.</p>
  <span class="btn">START YOUR COFFEE SUBSCRIPTION</span>
</div>
<svg class="abs" style="top:640px;left:0" width="1200" height="200" viewBox="0 0 1200 200">
  <path d="M0 60 C300 170 700 150 1200 40 L1200 200 L0 200Z" fill="#fff"/>
  <path d="M0 60 C300 170 700 150 1200 40" fill="none" stroke="#f2a531" stroke-width="10"/>
</svg>
<div class="photo" style="top:520px;left:860px;width:260px;height:240px;border-radius:50%;background:radial-gradient(circle at 50% 45%,#e9d3b8 0 30%,#9b6a45 31% 45%,#fff 46% 70%,#ddd 71%)" role="img" aria-label="Cup of cappuccino on a saucer with coffee beans"></div>

<h2 class="abs section-title" style="top:888px">How is Coffee Different from<br>Other Brands?</h2>
<div class="abs diff-band"></div>
<div class="photo" style="top:1072px;left:470px;width:260px;height:400px;background:linear-gradient(180deg,#7a4a30 0%,#3f2418 55%,#5a3322 100%);border-radius:10px 10px 30px 30px" role="img" aria-label="Coffee pouring into a patterned paper cup"></div>

<div class="abs feature" style="top:1130px;left:120px">
  <svg class="ficon" viewBox="0 0 34 34" fill="none" stroke="#d9622b" stroke-width="2"><path d="M6 28C6 14 16 6 28 6c0 14-8 22-22 22z"/><path d="M6 28L20 14"/></svg>
  <div><h4>Always Organic</h4><p>Aenean sollicitudin bibendum auctor elit volutpat.</p></div>
</div>
<div class="abs feature" style="top:1240px;left:120px">
  <svg class="ficon" viewBox="0 0 34 34" fill="none" stroke="#d9622b" stroke-width="2"><ellipse cx="17" cy="17" rx="9" ry="13" transform="rotate(30 17 17)"/><path d="M12 8c6 6 4 12 10 18"/></svg>
  <div><h4>Specialty-Grade</h4><p>Aenean sollicitudin bibendum auctor elit volutpat.</p></div>
</div>
<div class="abs feature" style="top:1350px;left:120px">
  <svg class="ficon" viewBox="0 0 34 34" fill="none" stroke="#d9622b" stroke-width="2"><path d="M5 24h24M8 24c0-6 4-10 9-10s9 4 9 10M17 10v4"/></svg>
  <div><h4>Zero Contaminants</h4><p>Aenean sollicitudin bibendum auctor elit volutpat.</p></div>
</div>
<div class="abs feature" style="top:1130px;left:790px">
  <svg class="ficon" viewBox="0 0 34 34" fill="none" stroke="#d9622b" stroke-width="2"><circle cx="17" cy="17" r="12"/><path d="M17 9v16M9 17h16"/></svg>
  <div><h4>Roasted for Health</h4><p>Aenean sollicitudin bibendum auctor elit volutpat.</p></div>
</div>
<div class="abs feature" style="top:1240px;left:790px">
  <svg class="ficon" viewBox="0 0 34 34" fill="none" stroke="#d9622b" stroke-width="2"><path d="M17 4l11 5v8c0 7-5 11-11 13-6-2-11-6-11-13V9z"/><path d="M12 17l4 4 7-8"/></svg>
  <div><h4>Antioxidant-Rich</h4><p>Aenean sollicitudin bibendum auctor elit volutpat.</p></div>
</div>
<div class="abs feature" style="top:1350px;left:790px">
  <svg class="ficon" viewBox="0 0 34 34" fill="none" stroke="#d9622b" stroke-width="2"><path d="M3 10h18v14H3zM21 15h6l4 5v4H21"/><circle cx="9" cy="26" r="2.5"/><circle cx="26" cy="26" r="2.5"/></svg>
  <div><h4>Delivered Fresh</h4><p>Aenean sollicitudin bibendum auctor elit volutpat.</p></div>
</div>

<!-- gift section -->
<svg class="abs" style="top:1600px;left:0" width="640" height="520" viewBox="0 0 640 520">
  <path d="M0 20 C180 -10 420 40 560 180 C660 290 600 440 470 500 C320 560 140 500 0 440Z" fill="#f2a531"/>
</svg>
<div class="photo" style="top:1610px;left:0;width:600px;height:470px;border-radius:0 60% 55% 0 / 0 50% 60% 0;background:linear-gradient(135deg,#6b3e22 0%,#a86a3c 40%,#e2a35a 70%,#7b4a2a 100%)" role="img" aria-label="Copper coffee pot and cup of coffee on a wooden table"></div>
<div class="abs copy" style="top:1656px;left:724px;width:400px">
  <div class="eyebrow">COFFEE BEANS</div>
  <h3>The Gift of Better<br>Mornings</h3>
  <p>Etiam rhoncus maecenas tempus, tellus eget condim entum rhon cus sem quam semper libero sit amet adipisc ing sem neque sed ipsum. Nam quam nunc blandit vel luctus pulvinar hendrerit id lorem. Maecenas nec odio et ante tincidunt tempus donec vitae sapien ut libero venenatis faucibus nullam quis ante.</p>
  <span class="btn">THE BEST COFFEE GIFTS</span>
</div>
<div class="photo" style="top:1990px;left:1000px;width:200px;height:170px;border-radius:50% 0 0 50%;background:radial-gradient(circle at 60% 50%,#6a3a20,#b07a4a 60%,rgba(255,255,255,0) 72%)" role="img" aria-label="Roasted coffee beans with dried leaves"></div>

<!-- why section -->
<section class="abs why"></section>
<h2 class="abs section-title" style="top:2160px">Why Mesa Alta Coffee is Love<br>at First Sip</h2>
<div class="abs card" style="top:2280px;left:160px">
  <div class="photo" style="background:linear-gradient(135deg,#b38b5a,#4d5a32 60%,#2e3a1f)" role="img" aria-label="Bag of specialty coffee on burlap"></div>
  <div class="body"><h4>Simply the Best<br>Coffees</h4><p>Aenean sollicitudin lorem auctor bibendum auctor nisi elit a duo consequat.</p></div>
</div>
<div class="abs card" style="top:2280px;left:460px">
  <div class="photo" style="background:linear-gradient(135deg,#d8c7b5,#8c6a52 55%,#3c2a20)" role="img" aria-label="Woman enjoying a cup of coffee"></div>
  <div class="body"><h4>Curated by a World-Class<br>Coffee Expert</h4><p>Aenean sollicitudin lorem auctor bibendum auctor nisi elit a duo consequat.</p></div>
</div>
<div class="abs card" style="top:2280px;left:760px">
  <div class="photo" style="background:linear-gradient(135deg,#ece6de,#b89a78 55%,#6a4a34)" role="img" aria-label="Coffee bags and cups on a counter"></div>
  <div class="body"><h4>Delivered at Peak<br>Freshness</h4><p>Aenean sollicitudin lorem auctor bibendum auctor nisi elit a duo consequat.</p></div>
</div>

<!-- difference section -->
<div class="abs copy" style="top:2820px;left:100px;width:540px">
  <div class="eyebrow">COFFEE BEANS</div>
  <h3>You Will Feel a Difference<br>After Drinking Mesa Alta<br>Coffee</h3>
  <p>Etiam rhoncus maecenas tempus, tellus eget condim entum rhon cus sem quam semper libero sit amet adipisc ing sem neque sed ipsum. Nam quam nunc blandit vel luctus pulvinar hendrerit id lorem. Maecenas nec odio et ante tincidunt tempus donec vitae sapien ut libero venenatis.</p>
</div>
<svg class="abs" style="top:2740px;left:680px" width="520" height="520" viewBox="0 0 520 520">
  <path d="M520 0 L520 500 C400 520 260 470 160 380 C40 270 60 120 180 50 C280 -10 420 0 520 0Z" fill="#f2a531"/>
</svg>
<div class="photo" style="top:2720px;left:700px;width:500px;height:500px;border-radius:60% 0 0 55% / 50% 0 0 60%;background:radial-gradient(circle at 55% 50%,#7a4a2a 0 25%,#3a2a22 45%,#5c4636 70%,#2a1e18)" role="img" aria-label="Cups of coffee and beans on a round wooden board"></div>
<div class="photo" style="top:3110px;left:0;width:200px;height:170px;border-radius:0 50% 50% 0;background:radial-gradient(circle at 35% 50%,#4a2414,#7a4024 50%,rgba(255,255,255,0) 72%)" role="img" aria-label="Pile of roasted coffee beans"></div>

<!-- band -->
<div class="abs band"><span>BEST DELICIOUS</span><span>COFFEE BEAN</span></div>
<div class="photo" style="top:3308px;left:478px;width:244px;height:244px;border-radius:50%;background:radial-gradient(circle,#e7cfae 0 28%,#a46a3e 29% 42%,#fff 43% 68%,#d8d8d8 69%)" role="img" aria-label="Latte with heart latte art seen from above"></div>

<!-- testimonial -->
<svg class="abs" style="top:3610px;left:540px" width="120" height="100" viewBox="0 0 120 100" fill="#e7e7e7"><path d="M10 90V50C10 25 25 10 50 6v16C35 26 30 36 30 50h20v40zM66 90V50c0-25 15-40 40-44v16c-15 4-20 14-20 28h20v40z"/></svg>
<p class="abs quote">I'm a testimonial. Click to edit me and add text that says something nice about you and your services.</p>
<div class="abs quote-name">RENA CALLOWAY</div>
<div class="abs dots"><i></i><i></i><i></i></div>
<div class="photo" style="top:3840px;left:1040px;width:160px;height:150px;border-radius:50% 0 0 50%;background:radial-gradient(circle at 60% 50%,#5a2e18,#8a5232 50%,rgba(255,255,255,0) 72%)" role="img" aria-label="Coffee beans spilling from a cup"></div>

<!-- posts -->
<h2 class="abs section-title" style="top:3960px">Latest Post Article</h2>
<div class="abs card" style="top:4040px;left:160px">
  <div class="photo" style="background:linear-gradient(135deg,#3a2418,#a0764e 55%,#2a1a12)" role="img" aria-label="Barista pouring latte art"></div>
  <div class="body"><div class="meta">by admin · January 2021</div><h4>Some blog heading goes here with des...</h4><p>Aenean sollicitudin lorem bibendum auctor nisi elit a duo consequat.</p></div>
</div>
<div class="abs card" style="top:4040px;left:460px">
  <div class="photo" style="background:linear-gradient(135deg,#6a3a20,#3a1e10 50%,#8a5a3a)" role="img" aria-label="Heap of roasted coffee beans"></div>
  <div class="body"><div class="meta">by admin · January 2021</div><h4>Some blog heading goes here with des...</h4><p>Aenean sollicitudin lorem bibendum auctor nisi elit a duo consequat.</p></div>
</div>
<div class="abs card" style="top:4040px;left:760px">
  <div class="photo" style="background:linear-gradient(135deg,#c79a72,#7a4a30 55%,#e0c2a4)" role="img" aria-label="Hands holding a cup of coffee"></div>
  <div class="body"><div class="meta">by admin · January 2021</div><h4>Some blog heading goes here with des...</h4><p>Aenean sollicitudin lorem bibendum auctor nisi elit a duo consequat.</p></div>
</div>

<!-- badges -->
<div class="abs badge" style="top:4540px;left:232px"></div>
<div class="abs badge" style="top:4540px;left:392px"></div>
<div class="abs badge" style="top:4540px;left:552px"></div>
<div class="abs badge" style="top:4540px;left:712px"></div>
<div class="abs badge" style="top:4540px;left:872px"></div>

<!-- footer -->
<svg class="abs" style="top:4720px;left:0" width="1200" height="624" viewBox="0 0 1200 624">
  <path d="M0 120 C260 200 520 30 820 60 C1000 80 1120 20 1200 0 L1200 624 L0 624Z" fill="#4a2516"/>
</svg>
<div class="photo" style="top:4690px;left:230px;width:280px;height:260px;border-radius:50%;background:radial-gradient(circle at 55% 45%,#e3c9a6 0 24%,#9a6238 25% 36%,#f4f0ea 37% 56%,#3a1c10 66%)" role="img" aria-label="Cappuccino with latte art on a saucer"></div>

<div class="abs" style="top:5060px;left:92px">
  <div class="brand brand-light">Mesa Alta Coffee</div>
  <div class="social"><span></span><span></span><span></span></div>
</div>
<div class="abs foot-col" style="top:4980px;left:370px">
  <h5>QUICK LINKS</h5>
  <ul><li>Home</li><li>Products</li><li>Gallery</li><li>Terms and Conditions</li><li>Contact Us</li><li>Support</li></ul>
</div>
<div class="abs foot-col" style="top:4980px;left:590px;width:220px">
  <h5>CONTACT US</h5>
  <div class="contact-item"><svg width="14" height="16" viewBox="0 0 14 16" fill="#f2a531"><path d="M7 0a6 6 0 0 1 6 6c0 4-6 10-6 10S1 10 1 6a6 6 0 0 1 6-6zm0 4a2 2 0 1 0 0 4 2 2 0 0 0 0-4z"/></svg><div><b>LOCATION</b>Some 456 Street<br>Brookfield East, Victoria 3057</div></div>
  <div class="contact-item"><svg width="14" height="14" viewBox="0 0 14 14" fill="#f2a531"><path d="M3 0l3 3-2 2c1 2 3 4 5 5l2-2 3 3-2 3C6 14 0 8 0 3z"/></svg><div><b>PHONE</b>Call us +00 12345 6789</div></div>
  <div class="contact-item"><svg width="14" height="12" viewBox="0 0 14 12" fill="none" stroke="#f2a531" stroke-width="1.5"><rect x="1" y="1" width="12" height="10"/><path d="M1 1l6 5 6-5"/></svg><div><b>EMAIL</b>hello@mesaaltacoffee.com</div></div>
</div>
<div class="abs foot-col" style="top:4980px;left:866px">
  <h5>INSTAGRAM</h5>
  <div class="insta">
    <div style="background:#8a5a3a" role="img" aria-label="Coffee cup photo"></div>
    <div style="background:#6a3e26" role="img" aria-label="Coffee beans photo"></div>
    <div style="background:#a87650" role="img" aria-label="Latte art photo"></div>
    <div style="background:#5a3424" role="img" aria-label="Cafe interior photo"></div>
    <div style="background:#b88a62" role="img" aria-label="Barista photo"></div>
    <div style="background:#7a4a30" role="img" aria-label="Espresso photo"></div>
  </div>
</div>
<div class="abs" style="top:5268px;left:92px;width:1016px;height:1px;background:rgba(255,255,255,.15)"></div>
<div class="abs copyright">© 2021 | MESA ALTA COFFEE. ALL RIGHTS RESERVED</div>
<div class="abs" style="top:5296px;left:1136px;width:34px;height:34px;border-radius:50%;background:var(--amber)"></div>

</body>
</html>
```